Personal Injury Law Firm Marketing Postcards

Looking for 4 different high quality graphic postcards (print on both sides of 4"x6" postcard to market a Personal Injury Lawyer (Walter Dunmore). These will be placed on cars and in stores on stands. My photo and/or stock images.... We are targeting People who have been injured in automobile accidents, motorcycle accidents, slip and fall (wet/greasy floors indoors in supermarkets, restaurants, etc., snow and ice outdoors on sidewalks) trip and fall cases on dangerous staircases. indoor/outdoor, dog bite injuries. ( I like the use of stock images of these type of injury causing accidents. You can use following language "Serving People Injured in NY & NJ" . Millions of Dollars Recovered, Free Consultation and No Fee Unless We Recover Money! Phone number to be displayed (555) 614-3082 "call or text" Available 24 hours a day 7 days per week. May also want to mention that we can take over your case from another lawyer if you are not satisfied with your current attorney. There should be a small space in corner which has a space for my marketing person to handwrite in their reference code.

Target Market(s)

18-75 years old - densely populated major city

Industry/Entity Type

Legal

Font styles to use
Other font styles liked:
• Please use logo style that I uploaded.. Please do not just cut parts of my website out and use them. Do not use LOGO from my website

Colors
0054AA
0677BA
7BADD7
CADEEF
E8F1F8
00AB8E
00BBA5
67D7C9
C6EFE9
E9F9F6

Requirements
Must have
• Professional Appearance

```html
<!DOCTYPE html>
<html lang="en">
<head>
<meta charset="utf-8">
<title>Walter Dunmore Postcards</title>
<link rel="stylesheet" href="https://fonts.googleapis.com/css2?family=Roboto+Condensed:wght@400;700&family=Roboto:ital,wght@0,400;0,500;1,500&display=swap">
<style>
  :root {
    --navy: #243165;
    --gold: #d2b06e;
    --white: #ffffff;
    --teal-light: #00a3c2;
    --teal-dark: #007e9e;
    --condensed: "Roboto Condensed", "Arial Narrow", sans-serif;
    --body: "Roboto", Arial, sans-serif;
  }
  * { box-sizing: border-box; margin: 0; padding: 0; }
  html, body { width: 1200px; height: 1000px; overflow: hidden; }
  body {
    background: radial-gradient(ellipse at 50% 45%, var(--teal-light), var(--teal-dark));
    position: relative;
    font-family: var(--body);
  }
  .postcard {
    position: absolute;
    left: 264px;
    width: 672px;
    height: 457px;
    overflow: hidden;
  }
  .postcard--front { top: 30px; background: var(--gold); }
  .postcard--back { top: 512px; background: var(--white); }

  /* Front */
  .front__header {
    position: absolute; left: 0; top: 43px; width: 672px; height: 83px;
    background: var(--navy); color: var(--white);
  }
  .front__headline {
    position: absolute; left: 300px; width: 332px; top: 6px;
    text-align: center; white-space: nowrap;
    font-family: var(--condensed); font-weight: 700; font-size: 23.5px; letter-spacing: -0.2px;
    line-height: 28px;
  }
  .front__tagline {
    position: absolute; left: 300px; width: 332px; top: 42px;
    text-align: center; white-space: nowrap;
    font-style: italic; font-weight: 500; font-size: 12.5px; line-height: 17px;
  }
  .front__portrait-panel {
    position: absolute; left: 0; top: 43px; width: 320px; height: 368px;
    background: var(--white); border-top-right-radius: 100px; overflow: hidden;
  }
  .front__portrait {
    position: absolute; left: 135px; top: 2px; width: 185px; height: 366px;
    background: linear-gradient(180deg, #8a7a6e 0%, #3d4a86 45%, #2a2f52 100%);
    border-radius: 80px 80px 0 0;
  }
  .brand {
    position: absolute; display: flex; align-items: center; gap: 5px;
    color: var(--gold); font-family: var(--body); font-weight: 500;
    text-transform: uppercase; text-align: center; line-height: 1.3;
    white-space: nowrap;
  }
  .brand__square { width: 9px; height: 9px; background: var(--gold); flex: none; }
  .front__brand { left: 24px; top: 140px; font-size: 9.5px; }
  .front__footer {
    position: absolute; left: 0; top: 411px; width: 320px; height: 46px;
    background: var(--navy); color: var(--white);
    display: flex; align-items: center; justify-content: center;
    font-size: 15px; font-weight: 500; letter-spacing: 5.5px; white-space: nowrap;
  }
  .photo { position: absolute; border: 3px solid var(--white); }
  .photo--car { left: 319px; top: 132px; width: 312px; height: 170px;
    background: linear-gradient(120deg, #a9b07a 0%, #7e8a9c 40%, #2b3b6a 75%, #55606e 100%); }
  .photo--slip { left: 319px; top: 311px; width: 146px; height: 131px;
    background: linear-gradient(160deg, #eceeee 0%, #c8cbcc 60%, #9a9d9f 100%); }
  .photo--ladder { left: 474px; top: 311px; width: 159px; height: 131px;
    background: linear-gradient(160deg, #e8e8e6 0%, #c9bfae 60%, #8c7a62 100%); }

  /* Back */
  .back__media-frame {
    position: absolute; left: 0; top: 29px; width: 334px; height: 428px;
    background: var(--navy); border-top-right-radius: 112px;
  }
  .back__photo {
    position: absolute; left: 0; top: 42px; width: 320px; height: 233px;
    background: linear-gradient(135deg, #8e8a84 0%, #b88a4e 45%, #d9b896 75%, #5a5f6e 100%);
    border-top-right-radius: 100px;
  }
  .back__info {
    position: absolute; left: 0; top: 275px; width: 320px; height: 182px;
    background: var(--gold); color: var(--navy);
  }
  .badge-247 { position: absolute; left: 49px; top: 3px; }
  .back__availability {
    position: absolute; left: 109px; top: 5px; white-space: nowrap;
    font-family: var(--condensed); font-weight: 700; font-size: 20px; line-height: 21px;
  }
  .back__note {
    position: absolute; left: 50px; top: 57px; white-space: nowrap;
    font-size: 11px; line-height: 13.5px;
  }
  .back__phone-icon { position: absolute; left: 49px; top: 104px; }
  .back__phone {
    position: absolute; left: 100px; top: 103px; white-space: nowrap;
    font-family: var(--condensed); font-weight: 700; font-size: 30px; line-height: 38px;
  }
  .back__brand { left: 346px; top: 75px; font-size: 10px; }
  .stamp-box {
    position: absolute; left: 538px; top: 46px; width: 87px; height: 87px;
    border: 1.5px solid var(--navy);
  }
  .address-line {
    position: absolute; left: 357px; width: 269px; height: 0;
    border-top: 1.5px solid var(--navy);
  }
  .back__web-band {
    position: absolute; left: 334px; top: 391px; width: 338px; height: 25px;
    background: var(--navy); color: var(--white);
    display: flex; align-items: center; justify-content: center;
    font-size: 15px; font-weight: 500; letter-spacing: 5.5px; white-space: nowrap;
  }
</style>
</head>
<body>

<section class="postcard postcard--front front">
  <div class="front__header">
    <h1 class="front__headline">Serving People Injured in NY &amp; NJ</h1>
    <p class="front__tagline">Millions of Dollars Recovered, Free Consultation<br>and No Fee Unless We Recover Money!</p>
  </div>
  <div class="front__portrait-panel">
    <div class="front__portrait" role="img" aria-label="Portrait of attorney Walter Dunmore in a navy suit"></div>
  </div>
  <div class="brand front__brand">
    <span class="brand__square"></span>
    <span>Law Office of<br>Walter Dunmore<br>P.C.</span>
  </div>
  <div class="front__footer">www.dunmorelegal.com</div>
  <div class="photo photo--car" role="img" aria-label="Rear-end collision between two cars"></div>
  <div class="photo photo--slip" role="img" aria-label="Man in suit slipping on a wet indoor floor"></div>
  <div class="photo photo--ladder" role="img" aria-label="Worker falling from a ladder outside a house"></div>
</section>

<section class="postcard postcard--back back">
  <div class="back__media-frame"></div>
  <div class="back__photo" role="img" aria-label="Aggressive dog biting a person's arm"></div>
  <div class="back__info">
    <svg class="badge-247" width="52" height="52" viewBox="0 0 52 52" aria-hidden="true">
      <path d="M26 4 A22 22 0 1 0 46 17" fill="none" stroke="#243165" stroke-width="3"/>
      <path d="M22 0 L30 4 L23 9 Z" fill="#243165"/>
      <circle cx="26" cy="28" r="17" fill="#243165"/>
      <text x="26" y="33" text-anchor="middle" fill="#ffffff" font-family="Roboto Condensed, sans-serif" font-weight="700" font-size="14">24/7</text>
    </svg>
    <p class="back__availability">Available 24 hours a day<br>7 days per week.</p>
    <p class="back__note">May also want to mention that we can take over<br>your case from another lawyer if you are not<br>satisfied with your current attorney</p>
    <svg class="back__phone-icon" width="42" height="42" viewBox="0 0 42 42" aria-hidden="true">
      <circle cx="21" cy="21" r="18" fill="none" stroke="#243165" stroke-width="3.5"/>
      <text x="21" y="27" text-anchor="middle" fill="#243165" font-family="Roboto Condensed, sans-serif" font-weight="700" font-size="16">or</text>
    </svg>
    <p class="back__phone">(555) 614-3082</p>
  </div>

  <div class="brand back__brand">
    <span class="brand__square"></span>
    <span>Law Office of<br>Walter Dunmore<br>P.C.</span>
  </div>
  <div class="stamp-box"></div>
  <div class="address-line" style="top:198px"></div>
  <div class="address-line" style="top:238px"></div>
  <div class="address-line" style="top:279px"></div>
  <div class="address-line" style="top:319px"></div>
  <div class="address-line" style="top:359px"></div>
  <div class="back__web-band">www.dunmorelegal.com</div>
</section>

</body>
</html>
```